Business Card for a Dental Office

The design should communicate integrity, quality and reliability. We also want the card look elegant, simple, but still stand out, different from the traditional-dental-office business card.

Business

```html
<!DOCTYPE html>
<html lang="en">
<head>
<meta charset="utf-8">
<title>Harbourline Dental Centre – Business Card</title>
<link rel="stylesheet" href="https://fonts.googleapis.com/css2?family=Source+Sans+3:wght@400;600;700&display=swap">
<style>
  :root {
    --bg: #e9e7e3;
    --card: #ffffff;
    --ink: #111111;
    --gold: #c9b11c;
    --gold-dark: #8a7a14;
    --yellow: #f3e51e;
    --band-black: #050505;
  }
  * { margin: 0; padding: 0; box-sizing: border-box; }
  html, body { width: 1200px; height: 1000px; overflow: hidden; }
  body {
    background: var(--bg);
    font-family: "Source Sans 3", "Helvetica Neue", Arial, sans-serif;
    color: var(--ink);
    position: relative;
  }
  .business-card {
    position: absolute;
    left: 67px;
    top: 182px;
    width: 666px;
    height: 397px;
    background: var(--card);
    transform: scale(1.6);
    transform-origin: top left;
    box-shadow: 0 1px 3px rgba(0,0,0,.18);
    overflow: hidden;
  }
  .brand { position: absolute; left: 33px; top: 84px; display: flex; align-items: flex-start; gap: 10px; }
  .brand-mark { width: 22px; height: 22px; background: var(--gold); margin-top: 6px; }
  .brand-name {
    font-weight: 700; font-size: 33px; line-height: 34px; letter-spacing: -0.5px;
    text-transform: uppercase; color: var(--ink);
  }
  .brand-tagline {
    position: absolute; left: 65px; top: 119px;
    font-size: 15.5px; font-weight: 600; letter-spacing: 0.6px;
    text-transform: uppercase; color: var(--gold-dark); line-height: 16px;
  }
  .holder { position: absolute; right: 33px; top: 203px; text-align: right; }
  .holder-name { font-weight: 700; font-size: 21px; line-height: 24px; }
  .holder-role { font-size: 16px; line-height: 20px; }
  .divider { position: absolute; left: 33px; top: 242px; width: 520px; height: 1.5px; background: var(--ink); }
  .accent-tab { position: absolute; left: 653px; top: 205px; width: 13px; height: 40px; background: var(--gold); }
  .address { position: absolute; left: 33px; top: 297px; font-size: 16px; line-height: 23px; font-style: normal; }
  .contacts { position: absolute; right: 33px; top: 274px; list-style: none; }
  .contacts li { display: flex; justify-content: flex-end; align-items: center; gap: 9px; font-size: 16px; line-height: 23px; }
  .contacts svg { width: 14px; height: 12px; fill: var(--gold); }
  .footer-band {
    position: absolute; left: 0; bottom: 0; width: 666px; height: 31px;
    background: linear-gradient(90deg, var(--band-black) 0 345px, var(--gold) 345px, var(--yellow) 75%, var(--gold) 100%);
  }
  .footer-mark { position: absolute; left: 355px; top: 9px; width: 13px; height: 13px; background: #ffffff; }
</style>
</head>
<body>
  <article class="business-card">
    <div class="brand">
      <span class="brand-mark"></span>
      <span class="brand-name">Harbourline Dental Centre</span>
    </div>
    <p class="brand-tagline">Caring for every smile with pride</p>

    <div class="holder">
      <p class="holder-name">Daniel Pryce, PHA</p>
      <p class="holder-role">President</p>
    </div>
    <div class="divider"></div>
    <div class="accent-tab"></div>

    <address class="address">
      Level 12, 48 Meridian House<br>
      Sydney, New South Wales
    </address>

    <ul class="contacts">
      <li>+ 000 000 0000
        <svg viewBox="0 0 14 12" aria-label="Phone"><path d="M1 4c0-2 3-3 6-3s6 1 6 3v1h-3V4H4v1H1z M3 6h8l2 5H1z"/></svg>
      </li>
      <li>+ 000 000 0000
        <svg viewBox="0 0 14 12" aria-label="Fax"><path d="M3 0h8v3H3z M0 4h14v5h-2V7H2v2H0z M3 8h8v4H3z"/></svg>
      </li>
      <li>info@harbourlinedental.com
        <svg viewBox="0 0 14 12" aria-label="Email"><path d="M0 1h14v1L7 7 0 2z M0 4l7 5 7-5v7H0z"/></svg>
      </li>
    </ul>

    <div class="footer-band"><span class="footer-mark"></span></div>
  </article>
</body>
</html>
```